Etiketten für besondere Frauen-Teemischungen
Top Design, zügige Reaktionszeit, sehr netter Kontakt. Alle Wünsche und Anmerkungen wurden perfekt umgesetzt und die Arbeit ist qualitativ hochwertig. Jederzeit gerne wieder! Vielen Dank für das hervorragende Design.
Zielgruppe
Ich stelle Teemischungen speziell für die Schwangerschaft und das Wochenbett sowie für Regelbeschwerden und Wechseljahre her. Zielgruppe sind also Frauen ab Kinderwunsch bis Klimakterium.
Name meiner Unternehmung ist 'Mohn-Quell'
Aufgabenstellung
Ich wünsche mir ein nostalgisches Design, abgelehnt an Apotheken um 1900.
Die Verpackung besteht aus Braunglastiegeln mit schwarzem Bakelitdeckel sowie Glasphiolen mit Korkverschluss.
In den Farben zurückhaltend, nicht knallig. gerne Elfenbein und Lindgrün.
In Anlehnung an den Namen wäre es schön (aber nicht zwingend notwendig), wenn ein Herz dezent eingebunden werden könnte.

```html
<!DOCTYPE html>
<html lang="de">
<head>
<meta charset="utf-8">
<title>Etiketten für Teemischungen – Mohn-Quell</title>
<link href="https://fonts.googleapis.com/css2?family=Montserrat:wght@400;600;700&family=Oswald:wght@500;600&family=Pinyon+Script&display=swap" rel="stylesheet">
<style>
  :root {
    --ink: #4a4a4a;
    --ink-soft: #6b6b6b;
    --ivory: #fbf8ef;
    --page: #ffffff;
    --caption: #a9a9a9;
    --edge: #ebe6da;
  }
  * { box-sizing: border-box; margin: 0; padding: 0; }
  html, body { width: 994px; height: 1200px; overflow: hidden; background: var(--page); }
  body { position: relative; font-family: "Montserrat", sans-serif; color: var(--ink); }

  .section-caption {
    position: absolute; top: 232px;
    font-size: 8px; letter-spacing: .22em; color: var(--caption); text-transform: uppercase;
  }
  .section-caption--tags { left: 50px; width: 456px; text-align: center; }
  .section-caption--labels { left: 620px; width: 300px; text-align: center; }

  /* Tag (Anhänger 60 x 60 mm) */
  .tag {
    position: absolute; width: 220px; height: 220px;
    background: var(--ivory); border: 1px solid var(--edge);
    font-size: 10px;
  }
  .frame { position: absolute; inset: .8em; border: .22em solid var(--ink); }
  .frame::after { content: ""; position: absolute; inset: .3em; border: .1em solid var(--ink); }

  .front {
    position: absolute; inset: 0;
    display: flex; flex-direction: column; align-items: center;
    padding-top: 2.5em; text-align: center;
  }
  .brand-name { font-weight: 600; font-size: .95em; letter-spacing: .32em; }
  .since { display: flex; align-items: center; gap: .9em; margin-top: .35em; }
  .since-word {
    font-size: .5em; letter-spacing: .15em;
    border-top: .1em solid var(--ink); border-bottom: .1em solid var(--ink);
    padding: .25em .6em;
  }
  .brand-circle { width: 3.3em; height: 3.3em; border-radius: 50%; border: .12em solid var(--ink); }
  .kind { font-size: .52em; font-weight: 600; letter-spacing: .16em; line-height: 1.35; margin-top: .9em; }
  .title { font-family: "Oswald", sans-serif; font-weight: 600; font-size: 2.45em; line-height: 1.1; letter-spacing: .02em; margin-top: .08em; }
  .title--long { font-size: 2.05em; margin-top: .25em; margin-bottom: .1em; }
  .flavour { font-size: .55em; font-weight: 600; letter-spacing: .25em; }
  .claim { font-family: "Pinyon Script", cursive; font-size: 1.45em; line-height: 1.05; margin-top: .45em; }
  .weight { font-family: "Oswald", sans-serif; font-weight: 500; font-size: 1.3em; margin-top: .25em; letter-spacing: .05em; }

  .back {
    position: absolute; inset: 0;
    display: flex; flex-direction: column; align-items: center;
    padding: 2.6em 2.4em 0; text-align: center;
  }
  .back-title { font-family: "Oswald", sans-serif; font-weight: 600; font-size: 1.55em; letter-spacing: .04em; }
  .back-sub { font-size: .5em; letter-spacing: .22em; line-height: 1.4; margin-top: .2em; }
  .back-copy { font-size: .74em; line-height: 1.33; margin-top: .7em; }
  .back-copy b { font-weight: 700; }
  .back-meta {
    width: 13.5em; margin-top: .9em;
    display: flex; align-items: center; justify-content: space-between;
    border-top: .1em solid var(--ink); border-bottom: .1em solid var(--ink);
    padding: .25em 0;
  }
  .back-meta span { font-size: .47em; letter-spacing: .2em; line-height: 1.5; }
  .seal { width: 2.6em; height: 2.6em; border-radius: 50%; border: .12em solid var(--ink); }
  .back-address { font-size: .72em; line-height: 1.4; margin-top: .7em; }
  .back-address b { font-weight: 700; }

  /* Etikett 45 x 80 mm */
  .label {
    position: absolute; width: 300px; height: 169px;
    background: var(--ivory); border: 1px solid var(--edge);
  }
  .label-info {
    position: absolute; left: 8px; top: 6px; width: 60px; height: 157px;
    writing-mode: vertical-rl; font-size: 6.4px; line-height: 1.3; text-align: justify;
  }
  .label-info b { font-weight: 700; }
  .label-panel {
    position: absolute; left: 72px; top: 5px; width: 160px; height: 159px;
    font-size: 7.1px;
  }
  .label-panel .frame { inset: 0; }
  .label-panel .front { padding-top: 2.1em; }
  .label-legal {
    position: absolute; left: 236px; top: 8px; width: 56px; height: 153px;
    writing-mode: vertical-rl; transform: rotate(180deg);
    font-size: 6.4px; line-height: 1.35; display: flex; justify-content: space-between;
  }
  .label-legal b { font-weight: 700; }

  .footer {
    position: absolute; top: 880px; left: 0; width: 994px; text-align: center;
    font-size: 7.5px; letter-spacing: .2em; color: var(--caption);
  }
</style>
</head>
<body>

  <p class="section-caption section-caption--tags">Anhänger 60 x 60 mm</p>
  <p class="section-caption section-caption--labels">Etiketten 45 x 80 mm</p>

  <!-- Wechseljahre: Anhänger Vorderseite -->
  <div class="tag" style="left:50px; top:280px;">
    <div class="frame"></div>
    <div class="front">
      <div class="brand-name">MOHNQUELL</div>
      <div class="since"><span class="since-word">SEIT</span><span class="brand-circle"></span><span class="since-word">2019</span></div>
      <div class="kind">TEEMISCHUNGEN<br>FÜR FRAUEN</div>
      <div class="title">WECHSELJAHRE</div>
      <div class="flavour">HIMBEERE HOLUNDER</div>
      <div class="claim">Teemischung zur Unterstützung<br>eines gesunden Zyklus</div>
      <div class="weight">50 G ℮</div>
    </div>
  </div>

  <!-- Wechseljahre: Anhänger Rückseite -->
  <div class="tag" style="left:286px; top:280px;">
    <div class="frame"></div>
    <div class="back">
      <div class="back-title">WECHSELJAHRE</div>
      <div class="back-sub">TEEMISCHUNG ZUR UNTERSTÜTZUNG<br>EINES GESUNDEN ZYKLUS</div>
      <p class="back-copy"><b>Zubereitung:</b> Teemischung mit kochendem Wasser aufgießen und 5-8 Minuten ziehen lassen. Nur so erhalten Sie ein sicheres Lebensmittel.<br><b>Zutaten:</b> Kurkuma (42%)*, Apfel (35%)*, Ingwer*, natürliches Aroma, *Zutaten stammen aus ökologischem Landbau</p>
      <div class="back-meta"><span>MOHN-QUELL<br>PREMIUM</span><span class="seal" role="img" aria-label="Rundes Siegel"></span><span>LOS-NR.<br>12345678</span></div>
      <p class="back-address">Mohn-Quell UG<br>Musterstraße 10 · 12345 Musterstadt<br><b>www.mohn-quell.de</b></p>
    </div>
  </div>

  <!-- Schwangerschaft: Anhänger Vorderseite -->
  <div class="tag" style="left:50px; top:560px;">
    <div class="frame"></div>
    <div class="front">
      <div class="brand-name">MOHNQUELL</div>
      <div class="since"><span class="since-word">SEIT</span><span class="brand-circle"></span><span class="since-word">2019</span></div>
      <div class="kind">TEEMISCHUNGEN<br>FÜR FRAUEN</div>
      <div class="title title--long">SCHWANGERSCHAFT</div>
      <div class="flavour">HIMBEERE HOLUNDER</div>
      <div class="claim">Teemischung zur Unterstützung<br>eines gesunden Zyklus</div>
      <div class="weight">50 G ℮</div>
    </div>
  </div>

  <!-- Schwangerschaft: Anhänger Rückseite -->
  <div class="tag" style="left:286px; top:560px;">
    <div class="frame"></div>
    <div class="back">
      <div class="back-title">SCHWANGERSCHAFT</div>
      <div class="back-sub">TEEMISCHUNG ZUR UNTERSTÜTZUNG<br>EINES GESUNDEN ZYKLUS</div>
      <p class="back-copy"><b>Zubereitung:</b> Teemischung mit kochendem Wasser aufgießen und 5-8 Minuten ziehen lassen. Nur so erhalten Sie ein sicheres Lebensmittel.<br><b>Zutaten:</b> Kurkuma (42%)*, Apfel (35%)*, Ingwer*, natürliches Aroma, *Zutaten stammen aus ökologischem Landbau</p>
      <div class="back-meta"><span>MOHN-QUELL<br>PREMIUM</span><span class="seal" role="img" aria-label="Rundes Siegel"></span><span>LOS-NR.<br>12345678</span></div>
      <p class="back-address">Mohn-Quell UG<br>Musterstraße 10 · 12345 Musterstadt<br><b>www.mohn-quell.de</b></p>
    </div>
  </div>

  <!-- Wechseljahre: Etikett -->
  <div class="label" style="left:620px; top:305px;">
    <p class="label-info"><b>Zubereitung:</b> Teemischung mit kochendem Wasser aufgießen und 5-8 Minuten ziehen lassen. Nur so erhalten Sie ein sicheres Lebensmittel. <b>Zutaten:</b> Kurkuma (42%)*, Apfel (35%)*, Ingwer*, natürliches Aroma, *Zutaten stammen aus ökologischem Landbau</p>
    <div class="label-panel">
      <div class="frame"></div>
      <div class="front">
        <div class="brand-name">MOHNQUELL</div>
        <div class="since"><span class="since-word">SEIT</span><span class="brand-circle"></span><span class="since-word">2019</span></div>
        <div class="kind">TEEMISCHUNGEN<br>FÜR FRAUEN</div>
        <div class="title">WECHSELJAHRE</div>
        <div class="flavour">HIMBEERE HOLUNDER</div>
        <div class="claim">Teemischung zur Unterstützung<br>eines gesunden Zyklus</div>
        <div class="weight">50 G ℮</div>
      </div>
    </div>
    <div class="label-legal">
      <span>Mindestens haltbar bis:</span>
      <span>Mohn-Quell UG<br>Musterstraße 10 · 12345 Musterstadt<br><b>www.mohn-quell.de</b><br>X000ABCDEFGH</span>
    </div>
  </div>

  <!-- Schwangerschaft: Etikett -->
  <div class="label" style="left:620px; top:585px;">
    <p class="label-info"><b>Zubereitung:</b> Teemischung mit kochendem Wasser aufgießen und 5-8 Minuten ziehen lassen. Nur so erhalten Sie ein sicheres Lebensmittel. <b>Zutaten:</b> Kurkuma (42%)*, Apfel (35%)*, Ingwer*, natürliches Aroma, *Zutaten stammen aus ökologischem Landbau</p>
    <div class="label-panel">
      <div class="frame"></div>
      <div class="front">
        <div class="brand-name">MOHNQUELL</div>
        <div class="since"><span class="since-word">SEIT</span><span class="brand-circle"></span><span class="since-word">2019</span></div>
        <div class="kind">TEEMISCHUNGEN<br>FÜR FRAUEN</div>
        <div class="title title--long">SCHWANGERSCHAFT</div>
        <div class="flavour">HIMBEERE HOLUNDER</div>
        <div class="claim">Teemischung zur Unterstützung<br>eines gesunden Zyklus</div>
        <div class="weight">50 G ℮</div>
      </div>
    </div>
    <div class="label-legal">
      <span>Mindestens haltbar bis:</span>
      <span>Mohn-Quell UG<br>Musterstraße 10 · 12345 Musterstadt<br><b>www.mohn-quell.de</b><br>X000ABCDEFGH</span>
    </div>
  </div>

  <p class="footer">ETIKETTEN FÜR TEEMISCHUNGEN „MOHN-QUELL“ · WWW.MOHN-QUELL.DE</p>

</body>
</html>
```